We are looking for an effective ad to recruit work from home Loan Officers for our Mortgage Brokerage.
Use the following text...
Earn Mortgage Income in your sleep. Its as easy as 1, 2, 3.....
1) Solicit Potential Applicants (Word of Mouth, Email, Social Media etc.)
2) Take Complete Applications & Submit Them
3) Wait to Get Paid.......(Avg. $2,500 per closing)
"You open the door, we'll finish the deal"
No Experience Necessary
No Goals or Quotas
No Office Hours / Work from Home Office
...and We Fully Reimburse ALL LICENSING FEES!!
Email Resume to mwelby@brightharborloans.example
Bright Harbor Lending Group, Inc.
947 W Caldwell Avenue, #318
Baltimore, MD 21230
NMLS #731860
www.brightharborloans.example
Phone (800) 555-0142
Licensed Mortgage Broker in MD and DC since 1997
Target Market(s)
Professionals looking to earn part time income at Loan Officers, preferably with strong social media following.
Industry/Entity Type
Loan
Look and feel

```html
<!DOCTYPE html>
<html lang="en">
<head>
<meta charset="utf-8">
<title>Bright Harbor Lending Group – Loan Officer Recruitment Flyer</title>
<link rel="stylesheet" href="https://fonts.googleapis.com/css2?family=Open+Sans:wght@400;600;700&family=Tinos:wght@400;700&display=swap">
<style>
  :root {
    --blue: #1a5fa8;
    --navy: #1d2b3a;
    --gold: #a8913a;
    --green: #9cc21a;
    --page: #e4e4e4;
    --text: #1f1f1f;
  }
  * { margin: 0; padding: 0; box-sizing: border-box; }
  html, body { width: 960px; height: 1200px; overflow: hidden; background: var(--page); }
  .flyer {
    position: absolute; left: 56px; top: 0; width: 848px; height: 1200px;
    background: #fff; overflow: hidden;
    font-family: "Open Sans", Arial, sans-serif; color: var(--text);
  }
  .flyer-shapes { position: absolute; inset: 0; }
  .abs { position: absolute; white-space: nowrap; }

  .brand { left: 622px; top: 100px; display: flex; align-items: center; gap: 10px; }
  .brand-dot { width: 26px; height: 26px; border-radius: 50%; background: var(--blue); flex: none; }
  .brand-name { font-weight: 700; font-size: 16px; line-height: 1.25; color: var(--blue); white-space: normal; width: 180px; }

  .headline-earn { left: 218px; top: 432px; font-family: "Tinos", "Times New Roman", serif; font-weight: 700; font-size: 86px; color: var(--blue); line-height: 1; }
  .headline-income { left: 68px; top: 524px; font-family: "Tinos", "Times New Roman", serif; font-weight: 700; font-size: 42px; color: var(--gold); line-height: 1; }
  .headline-sleep { left: 68px; top: 573px; font-family: "Tinos", "Times New Roman", serif; font-size: 36px; color: var(--blue); line-height: 1; }
  .headline-steps { left: 68px; top: 617px; font-family: "Tinos", "Times New Roman", serif; font-weight: 700; font-size: 42px; color: var(--gold); line-height: 1; }

  .step-list { left: 68px; top: 676px; list-style: none; font-size: 18px; line-height: 28px; }
  .step-num { color: var(--blue); font-weight: 700; }
  .step-note { font-size: 14px; }
  .step-pay { color: var(--gold); font-weight: 700; font-size: 16px; }

  .slogan { left: 68px; top: 772px; font-weight: 700; font-size: 30px; color: var(--blue); letter-spacing: -0.3px; }

  .perk-list { left: 70px; top: 820px; list-style: none; font-size: 17px; line-height: 25px; }
  .perk-list li { display: flex; align-items: center; gap: 10px; }
  .perk-list strong { font-weight: 700; }
  .tick { width: 14px; height: 14px; }

  .reimburse { left: 68px; top: 902px; font-size: 23px; color: var(--text); }
  .reimburse strong { color: var(--blue); font-weight: 700; }
  .email-line { left: 68px; top: 946px; font-size: 17px; font-weight: 700; color: var(--text); }
  .email-line span { color: var(--blue); }

  .footer-company { left: 68px; top: 1024px; font-weight: 700; font-size: 18px; color: var(--navy); }
  .footer-address { left: 68px; top: 1056px; font-size: 15px; line-height: 24px; color: var(--navy); }
  .footer-address div { display: flex; align-items: center; gap: 8px; }
  .icon { width: 14px; height: 14px; flex: none; }
  .social-badge { left: 404px; top: 1060px; width: 96px; height: 32px; background: #fff; border: 2px solid var(--blue); border-radius: 3px; }
  .footer-phone { left: 344px; top: 1106px; font-weight: 700; font-size: 20px; color: var(--navy); display: flex; align-items: center; gap: 10px; }
  .footer-web { left: 346px; top: 1138px; font-size: 14px; color: var(--navy); display: flex; align-items: center; gap: 8px; }
  .footer-license { left: 68px; top: 1160px; font-weight: 700; font-size: 19px; color: var(--navy); }
</style>
</head>
<body>
<main class="flyer">
  <svg class="flyer-shapes" width="848" height="1200" viewBox="0 0 848 1200">
    <defs>
      <radialGradient id="panelGrad" cx="0.45" cy="0.45" r="0.7">
        <stop offset="0" stop-color="#ffffff"/>
        <stop offset="1" stop-color="#dcdcdc"/>
      </radialGradient>
      <linearGradient id="teamGrad" x1="0" y1="0" x2="1" y2="1">
        <stop offset="0" stop-color="#f6f3f0"/>
        <stop offset="0.5" stop-color="#c9b3a3"/>
        <stop offset="1" stop-color="#2c3240"/>
      </linearGradient>
      <linearGradient id="cashGrad" x1="0" y1="0" x2="1" y2="1">
        <stop offset="0" stop-color="#f2eeea"/>
        <stop offset="0.6" stop-color="#e48a8c"/>
        <stop offset="1" stop-color="#6b4a3c"/>
      </linearGradient>
      <linearGradient id="deskGrad" x1="0" y1="0" x2="1" y2="1">
        <stop offset="0" stop-color="#f3f2ee"/>
        <stop offset="0.6" stop-color="#c9c7b8"/>
        <stop offset="1" stop-color="#6c4a2e"/>
      </linearGradient>
    </defs>

    <rect class="team-photo" x="0" y="0" width="600" height="470" fill="url(#teamGrad)" role="img" aria-label="Photo of two smiling business professionals in suits"/>

    <path class="content-panel" d="M0,470 Q300,355 848,390 L848,1200 L0,1200 Z" fill="url(#panelGrad)"/>
    <path class="swoosh-top-blue" d="M0,478 Q300,360 640,392" fill="none" stroke="var(--blue)" stroke-width="20"/>
    <path class="swoosh-top-white" d="M0,498 Q300,382 640,412" fill="none" stroke="#ffffff" stroke-width="6"/>
    <path class="swoosh-right-blue" d="M770,560 Q848,640 848,780 L848,560 Z" fill="var(--blue)"/>
    <path class="swoosh-right-green" d="M780,590 Q832,650 836,760" fill="none" stroke="var(--green)" stroke-width="8"/>

    <circle cx="650" cy="503" r="172" fill="var(--green)"/>
    <circle cx="650" cy="503" r="162" fill="#ffffff"/>
    <circle class="cash-photo" cx="650" cy="503" r="150" fill="url(#cashGrad)" role="img" aria-label="Photo of an excited woman holding a fan of cash"/>

    <path class="swoosh-bottom-blue" d="M0,1002 Q320,940 848,1044" fill="none" stroke="var(--blue)" stroke-width="16"/>
    <path class="swoosh-bottom-white" d="M0,1014 Q320,954 848,1058" fill="none" stroke="#ffffff" stroke-width="6"/>
    <path class="footer-band" d="M0,1018 Q320,960 848,1062 L848,1200 L0,1200 Z" fill="var(--green)"/>

    <circle cx="680" cy="1032" r="130" fill="var(--blue)"/>
    <circle cx="680" cy="1032" r="122" fill="#ffffff"/>
    <circle class="desk-photo" cx="680" cy="1032" r="112" fill="url(#deskGrad)" role="img" aria-label="Photo of a mortgage document with cash, a gavel and a magnifying glass"/>
  </svg>

  <div class="abs brand">
    <span class="brand-dot"></span>
    <span class="brand-name">Bright Harbor Lending Group, Inc.</span>
  </div>

  <h1 class="abs headline-earn">Earn</h1>
  <div class="abs headline-income">Mortgage Income</div>
  <div class="abs headline-sleep">in your sleep</div>
  <div class="abs headline-steps">Its as easy as 1, 2, 3.....</div>

  <ol class="abs step-list">
    <li><span class="step-num">1)</span> Solicit Potential Applicants <span class="step-note">(Word of Mouth, Email, Social Media etc.)</span></li>
    <li><span class="step-num">2)</span> Take Complete Applications &amp; Submit Them</li>
    <li><span class="step-num">3)</span> Wait to Get Paid.......<span class="step-pay">(Avg. $2,500 per closing)</span></li>
  </ol>

  <p class="abs slogan">"You open the door, we'll finish the deal"</p>

  <ul class="abs perk-list">
    <li><svg class="tick" viewBox="0 0 14 14"><path d="M1,7 L5,11 L13,2" fill="none" stroke="var(--gold)" stroke-width="2"/></svg><span><strong>No</strong> Experience Necessary</span></li>
    <li><svg class="tick" viewBox="0 0 14 14"><path d="M1,7 L5,11 L13,2" fill="none" stroke="var(--gold)" stroke-width="2"/></svg><span><strong>No</strong> Office Hours / Work from Home Office</span></li>
    <li><svg class="tick" viewBox="0 0 14 14"><path d="M1,7 L5,11 L13,2" fill="none" stroke="var(--gold)" stroke-width="2"/></svg><span><strong>No</strong> Goals or Quotas</span></li>
  </ul>

  <p class="abs reimburse">We Fully Reimburse <strong>ALL LICENSING FEES!!</strong></p>
  <p class="abs email-line">Email Resume to - <span>mwelby@brightharborloans.example</span></p>

  <div class="abs footer-company">Bright Harbor Lending Group, Inc.</div>
  <div class="abs footer-address">
    <div><svg class="icon" viewBox="0 0 14 14"><path d="M7,1 C4,1 2.5,3 2.5,5.2 C2.5,8.5 7,13 7,13 C7,13 11.5,8.5 11.5,5.2 C11.5,3 10,1 7,1 Z" fill="var(--blue)"/><circle cx="7" cy="5.2" r="1.6" fill="var(--green)"/></svg>947 W Caldwell Avenue, #318</div>
    <div style="padding-left:22px">Baltimore, MD 21230</div>
    <div style="padding-left:22px">NMLS #731860</div>
  </div>
  <div class="abs social-badge"></div>
  <div class="abs footer-phone"><svg class="icon" viewBox="0 0 14 14" style="width:18px;height:18px"><circle cx="7" cy="7" r="6.2" fill="none" stroke="var(--navy)" stroke-width="1.4"/><path d="M4.5,4 L5.8,3.8 L6.4,5.6 L5.6,6.2 Q6.4,7.8 7.8,8.5 L8.4,7.7 L10.2,8.3 L10,9.6 Q6.5,10 4.5,4 Z" fill="var(--navy)"/></svg>(800) 555-0142</div>
  <div class="abs footer-web"><svg class="icon" viewBox="0 0 14 14"><circle cx="7" cy="7" r="6" fill="var(--blue)"/></svg>www.brightharborloans.example</div>
  <div class="abs footer-license">Licensed Mortgage Broker in MD and DC since 1997</div>
</main>
</body>
</html>
```